Cognitive therapist.

I am a therapist and my main work is with clients who have depression and anxiety disorders.

I need something reasonably plain. Cognitive therapy is a very pragmatic approach to dealing with problems, so it isn't new agey (no offence to new age therapies at all)

Hi everyone, I am currently looking at a particular design that I will most likely go with. Cheers, Lyn

Lyn Marchet
Cognitive Therapist
BA, PG Dip Mental Health,
PG Dip Cog Beh Therapy
MKRPG

The Quillan Rooms,
Level One
47 Harwick Parade
Cnr Drayfield St & Harwick Parade
P O Box 38 215
WELLINGTON 6287

Phone: 027 463 2851 Email: lmarchet@quorvane.co.nz

www.lynmarchet.co.nz

• No illustration, or colour. not old style fonts.

```html
<!DOCTYPE html>
<html lang="en">
<head>
<meta charset="utf-8">
<title>Lyn Marchet – Business Card</title>
<link rel="stylesheet" href="https://fonts.googleapis.com/css2?family=Montserrat:wght@600&family=Questrial&display=swap">
<style>
  :root {
    --teal: #6cc7b6;
    --grey-bar: #8a8a8c;
    --text-grey: #7d7d7f;
    --divider: #a9a9ab;
    --card: #ffffff;
    --page: #ecebe8;
  }
  * { margin: 0; padding: 0; box-sizing: border-box; }
  html, body { width: 1200px; height: 1000px; overflow: hidden; }
  body {
    background: var(--page);
    font-family: "Questrial", "Century Gothic", sans-serif;
    color: var(--text-grey);
    position: relative;
  }
  .card {
    position: absolute;
    left: 250px;
    width: 700px;
    height: 400px;
    background: var(--card);
    border-radius: 28px;
    overflow: hidden;
    box-shadow: 0 6px 18px rgba(0,0,0,0.12);
  }
  .card--teal { top: 60px; }
  .card--grey { top: 540px; }

  .bar { position: absolute; height: 10px; }
  .bar--top { left: 592px; right: 0; top: 240px; }
  .bar--bottom { left: 0; width: 305px; top: 334px; }
  .card--teal .bar { background: var(--teal); }
  .card--grey .bar { background: var(--grey-bar); }

  .identity {
    position: absolute;
    right: 372px;
    top: 150px;
    text-align: right;
    white-space: nowrap;
  }
  .identity__name {
    font-family: "Montserrat", "Century Gothic", sans-serif;
    font-weight: 600;
    font-size: 34px;
    letter-spacing: 0.5px;
    line-height: 1;
    color: var(--teal);
    text-transform: uppercase;
  }
  .identity__credentials {
    font-size: 17px;
    line-height: 20px;
    margin-top: 3px;
  }

  .divider {
    position: absolute;
    left: 342px;
    top: 82px;
    width: 1.5px;
    height: 148px;
    background: var(--divider);
  }

  .contact {
    position: absolute;
    left: 356px;
    top: 80px;
    font-size: 13.5px;
    line-height: 18px;
    white-space: nowrap;
  }
  .contact__postal b { font-family: "Montserrat", sans-serif; font-weight: 600; font-size: 12.5px; }
  .contact__line {
    display: flex;
    align-items: center;
    gap: 5px;
    margin-top: 3px;
  }
  .contact__icon { width: 15px; height: 15px; flex: none; }

  .website {
    position: absolute;
    left: 318px;
    top: 266px;
    font-size: 24px;
    line-height: 1;
    letter-spacing: 0.6px;
    white-space: nowrap;
  }
  .card--teal .website { color: var(--text-grey); }
  .card--grey .website { color: var(--teal); }
</style>
</head>
<body>

<section class="card card--teal">
  <div class="identity">
    <h1 class="identity__name">Lyn Marchet</h1>
    <p class="identity__credentials">Cognitive Therapist BA,<br>PG Dip Mental Health,<br>PG Dip Cog Beh Therapy MKRPG</p>
  </div>
  <div class="divider"></div>
  <div class="contact">
    <p class="contact__postal">The Quillan Rooms, Level One<br>47 Harwick Parade Cnr Drayfield St<br>&amp; Harwick Parade<br><b>P O Box</b> 38 215 WELLINGTON 6287</p>
    <p class="contact__line">
      <svg class="contact__icon" viewBox="0 0 16 16" aria-hidden="true"><circle cx="8" cy="8" r="8" fill="var(--teal)"/><rect x="5.5" y="3.5" width="5" height="9" rx="1" fill="none" stroke="#fff" stroke-width="1.2"/><circle cx="8" cy="10.6" r="0.7" fill="#fff"/></svg>
      027 463 2851
    </p>
    <p class="contact__line">
      <svg class="contact__icon" viewBox="0 0 16 16" aria-hidden="true"><circle cx="8" cy="8" r="8" fill="var(--teal)"/><rect x="4" y="5" width="8" height="6" fill="none" stroke="#fff" stroke-width="1.2"/><path d="M4 5 L8 8.5 L12 5" fill="none" stroke="#fff" stroke-width="1.2"/></svg>
      lmarchet@quorvane.co.nz
    </p>
  </div>
  <div class="bar bar--top"></div>
  <p class="website">www.lynmarchet.co.nz</p>
  <div class="bar bar--bottom"></div>
</section>

<section class="card card--grey">
  <div class="identity">
    <h2 class="identity__name">Lyn Marchet</h2>
    <p class="identity__credentials">Cognitive Therapist BA,<br>PG Dip Mental Health,<br>PG Dip Cog Beh Therapy MKRPG</p>
  </div>
  <div class="divider"></div>
  <div class="contact">
    <p class="contact__postal">The Quillan Rooms, Level One<br>47 Harwick Parade Cnr Drayfield St<br>&amp; Harwick Parade<br><b>P O Box</b> 38 215 WELLINGTON 6287</p>
    <p class="contact__line">
      <svg class="contact__icon" viewBox="0 0 16 16" aria-hidden="true"><circle cx="8" cy="8" r="8" fill="var(--teal)"/><rect x="5.5" y="3.5" width="5" height="9" rx="1" fill="none" stroke="#fff" stroke-width="1.2"/><circle cx="8" cy="10.6" r="0.7" fill="#fff"/></svg>
      027 463 2851
    </p>
    <p class="contact__line">
      <svg class="contact__icon" viewBox="0 0 16 16" aria-hidden="true"><circle cx="8" cy="8" r="8" fill="var(--teal)"/><rect x="4" y="5" width="8" height="6" fill="none" stroke="#fff" stroke-width="1.2"/><path d="M4 5 L8 8.5 L12 5" fill="none" stroke="#fff" stroke-width="1.2"/></svg>
      lmarchet@quorvane.co.nz
    </p>
  </div>
  <div class="bar bar--top"></div>
  <p class="website">www.lynmarchet.co.nz</p>
  <div class="bar bar--bottom"></div>
</section>

</body>
</html>
```